Business card design for Luxury Real Estate

Using the corporate logo you have designed, please design a business card for a luxury real estate company in Thailand.

The brand is about elegance, calm, sophistication and luxury. The card should look clean, modern and be standard business card size. The background should be white to enable future scanning of the card (funky backgrounds result in poor card scanning results).

Text on Business Card (Front side) shall include the following:
- Corporate Logo
- Include the following business services underneath " Sales. Rentals. Investments. Financing."
- Name: Marisa Tevel
- Title: CEO, Founder
- mobile phone: +65 84219637 (Singapore), +66 7000 48261 (Thailand)
- email: marisa@goldenreedhaven.com
- skype: goldenreedhaven
- url: www.goldenreedhaven.com

Backside
- include same info but shall have Chinese name and title.

please use the attached additional language in mandarin for "sales. rentals. investments. financing."

Normal 0 false false false EN-US JA X-NONE 售和房租。投和融    

Target Market(s)

high net worth individuals, business men/ women, finance managers.

Industry/Entity Type

Real Estate

Requirements
Must have
• elegant, sophisticated, clean, modern look. appealing but comforting to the eye. should not be crowded and overcomplicated.

```html
<!DOCTYPE html>
<html lang="en">
<head>
<meta charset="utf-8">
<title>Golden Reed Haven – Business Card</title>
<link rel="stylesheet" href="https://fonts.googleapis.com/css2?family=Tenor+Sans&family=Noto+Sans+SC:wght@400&display=swap">
<style>
  :root {
    --backdrop: #2b2b2b;
    --card: #ffffff;
    --ink: #1f1f1f;
    --gold: #b59a5e;
    --grey: #9b9b9b;
    --rule: #4a4a4a;
  }
  * { box-sizing: border-box; margin: 0; padding: 0; }
  html, body {
    width: 1200px; height: 900px; overflow: hidden;
    background: var(--backdrop);
    font-family: "Tenor Sans", "Optima", sans-serif;
  }
  .canvas {
    width: 1200px; height: 900px;
    display: flex; align-items: center; justify-content: center; gap: 60px;
  }
  .card {
    position: relative;
    width: 510px; height: 292px;
    background: var(--card);
    border-radius: 30px;
    box-shadow: 0 14px 30px rgba(0,0,0,0.45);
  }
  .cjk { font-family: "Noto Sans SC", sans-serif; }

  /* brand name */
  .brand {
    display: flex; align-items: center; gap: 10px;
    color: var(--ink);
    white-space: nowrap;
  }
  .brand-dot {
    width: 10px; height: 10px; border-radius: 50%;
    background: var(--gold);
  }

  /* front */
  .card--front .brand {
    position: absolute; left: 0; right: 0; top: 104px;
    justify-content: center; font-size: 38px;
  }
  .services {
    position: absolute; left: 0; right: 0; top: 196px;
    text-align: center; font-size: 17px; color: var(--ink);
  }
  .services .alt { color: var(--gold); }
  .services .stop { color: var(--gold); }

  /* back */
  .identity { position: absolute; left: 34px; top: 38px; }
  .person-name { font-size: 25px; color: var(--gold); }
  .person-name-cn { font-size: 15px; color: var(--ink); margin-top: 2px; }
  .person-title { font-size: 15px; color: var(--gold); margin-top: 12px; }
  .person-title-cn { font-size: 14px; color: var(--ink); margin-top: 1px; }

  .card--back .brand {
    position: absolute; right: 34px; top: 58px; font-size: 25px; gap: 8px;
  }
  .card--back .brand-dot { width: 8px; height: 8px; }

  .contact-list {
    position: absolute; left: 34px; top: 200px;
    list-style: none; font-size: 13px; line-height: 21px; color: var(--ink);
  }
  .contact-list .label { color: var(--gold); font-size: 12px; }

  .phones {
    position: absolute; left: 320px; top: 222px;
    font-size: 14px; line-height: 22px; color: var(--ink);
  }
  .phones .heading { color: var(--gold); font-size: 12.5px; margin-left: 6px; }
  .phones .region { color: var(--gold); font-size: 13px; }
</style>
</head>
<body>
<main class="canvas">
  <section class="card card--front">
    <div class="brand"><span class="brand-dot"></span><span class="brand-name">Golden Reed Haven</span></div>
    <p class="services">Sales<span class="stop">.</span> <span class="alt">Rentals.</span> Investments<span class="stop">.</span> <span class="alt">Financing.</span></p>
  </section>

  <section class="card card--back">
    <div class="identity">
      <p class="person-name">Marisa Tevel</p>
      <p class="person-name-cn cjk">戴美莎</p>
      <p class="person-title">CEO, Founder</p>
      <p class="person-title-cn cjk">总裁</p>
    </div>
    <div class="brand"><span class="brand-dot"></span><span class="brand-name">Golden Reed Haven</span></div>
    <ul class="contact-list">
      <li><span class="label">email:</span> marisa@goldenreedhaven.com</li>
      <li><span class="label">skype:</span> goldenreedhaven</li>
      <li><span class="label">web:</span> www.goldenreedhaven.com</li>
    </ul>
    <div class="phones">
      <p class="heading">mobile phones:</p>
      <p><span class="region">(Singapore)</span> +65 84219637</p>
      <p><span class="region">(Thailand)</span> +66 7000 48261</p>
    </div>
  </section>
</main>
</body>
</html>
```